Electrical & Communications Company Wordpress Themed Website Design

Hi everyone,

I need a wordpress themed website designed for a new company based in Sydney Australia called "VELTRIX". It delivers electrical and communication services to the domestic and commercial sectors.

It needs to be the FULL/COMPLETE wordpress theme! A clean and easy to use site.

Please guys take the time to look at these competitors sites:

www.tapnovo.com.au
www.harbelwiring.com.au
www.qul.com.au
www.lumavoltics.com.au
www.corbinwiring.com.au
www.fendrasparkies.com.au

Please use these site for ideas only!!! we want to be original.

(If you would like to add electrical and communications to the logo that is O.K.)

Note: These logo's are registered trademarks of veltrix pty ltd.

Accreditation:

Ubta member (Federated wiring and signalling guild)

PLEASE CHECK THE WEB PLANNING LAYOUT BELOW FOR ROUGH IDEA
Updates

Have requested to increase payment to $400 and now guarantee payment!

Hi guys, forgot to mention i would like to see the business phone number prominently some where with a call to action.As we are a service business and need people to easly be able to see our contact number. Maybe top right courner but open to ideas. 

 Guys/Girls this is for a complete working word press theme that i can load up on the sever and access thru wordpress admin. Code etc

Industry/Entity Type

Communications

Requirements
Must have
• - Logo Provided must be used
• - Themes and colours to be consisted with with brand
• - Fully customizable
• - Have a social share button from shariq.com
• - Must be the full/complete theme for word press
Nice to have
• - pixtorvault
• - contactform
• - would like zenda orbit pay quidlo displayed
• - Guarantee logo or something
Should not have
• - Please don't waste your or our time submitting templates or copies of other sites original only!

```html
<!DOCTYPE html>
<html lang="en">
<head>
<meta charset="utf-8">
<title>Veltrix — Electrical &amp; Communications</title>
<link href="https://fonts.googleapis.com/css2?family=Questrial&family=Arimo:wght@400;700&display=swap" rel="stylesheet">
<style>
:root{
  --page:#000;
  --panel:#0d0d10;
  --red:#e0200f;
  --red-dark:#b01204;
  --accent:#ff1a1a;
  --text:#d8d8d8;
  --muted:#9a9a9a;
  --white:#fff;
  --line:#5a5a5a;
  --silver-top:#f4f4f4;
  --silver-bot:#b9b9b9;
}
*{box-sizing:border-box;margin:0;padding:0}
html,body{width:1036px;height:1200px;overflow:hidden;background:var(--page)}
body{position:relative;font-family:"Arimo",Arial,sans-serif;color:var(--text)}
.abs{position:absolute}
.display{font-family:"Questrial","Century Gothic",sans-serif;letter-spacing:2px}
.hl{color:var(--accent)}

.backdrop{left:24px;top:0;width:987px;height:1060px;background:radial-gradient(ellipse at 60% 30%,#15151c 0%,#08080b 60%,#000 100%)}

.masthead{left:49px;top:0;width:931px;height:95px;border-radius:0 0 14px 14px;background:linear-gradient(var(--silver-top),var(--silver-bot))}
.brand{left:56px;top:26px;display:flex;align-items:center;gap:10px;font-family:"Questrial",sans-serif;font-size:36px;color:#4a4a4a;letter-spacing:1px}
.brand-dot{width:30px;height:30px;border-radius:50%;background:var(--red)}
.social{top:38px;width:28px;height:28px;border-radius:4px}
.social.feed{left:599px;background:#e8801e}
.social.one{left:647px;background:#6aa9cf}
.social.two{left:695px;background:#3b5a97}
.callout{left:765px;top:28px;width:196px;height:48px;border-radius:8px;background:linear-gradient(#ff4a3a,var(--red-dark));border:1px solid #ff8a80;display:flex;align-items:center;gap:10px;padding-left:22px;color:var(--white);font-weight:700;font-size:18px;letter-spacing:1px}
.callout svg{flex:none}

.nav{left:52px;top:119px;width:928px;height:40px;border-radius:5px;background:linear-gradient(#e83218,var(--red-dark));display:flex;align-items:center;padding-left:18px;gap:0}
.nav a{color:var(--white);text-decoration:none;font-size:14px;letter-spacing:1px;padding:4px 11px}
.nav a.current{background:var(--red);font-weight:700}

.feature-photo{left:378px;top:158px;width:632px;height:335px;background:radial-gradient(ellipse at 45% 45%,#f0b040 0%,#a63a10 25%,#3a1508 55%,#120707 100%)}
.slider{left:52px;top:188px;width:551px;height:269px;border-radius:14px;background:#fbe9f2;padding:12px}
.slide{width:100%;height:100%;background:linear-gradient(100deg,#2a2a2a 0%,#6a6058 35%,#c7bfb8 60%,#e86a2a 80%,#d0d0d0 100%)}
.arrow{top:315px;width:24px;height:24px;border-radius:50%;background:var(--white);display:flex;align-items:center;justify-content:center}
.perk{left:630px;width:349px;height:72px;border-radius:12px;border:1px solid #aaa;background:linear-gradient(rgba(255,255,255,.35),rgba(40,20,20,.6) 50%,rgba(10,5,5,.8));display:flex;align-items:center;justify-content:center;color:#eee;font-size:25px}

.section-title{font-size:25px;color:var(--white)}
.copy{font-size:13.5px;line-height:17px;letter-spacing:.8px;color:var(--text)}
.more{width:58px;height:15px;border-radius:3px;background:linear-gradient(#eee,#aaa);color:#222;font-size:11px;display:flex;align-items:center;justify-content:center;gap:3px}

.box{border:1px solid var(--line);border-radius:14px;background:linear-gradient(#3a3a3a,#0a0a0a 45%,#000)}
.field{left:33px;width:273px;height:40px;background:var(--white);color:#111;font-size:18px;letter-spacing:1px;padding:8px 16px}
.btn{height:30px;border-radius:15px;background:linear-gradient(#555,#000);border:1px solid #999;color:var(--white);font-size:18px;letter-spacing:1px;display:flex;align-items:center;justify-content:center}
.avatar{left:16px;width:85px;height:63px;border-radius:12px;border:1px solid #777;background:linear-gradient(#777,#111 50%,#000)}

.payments{left:57px;top:1062px;width:82px;height:31px;background:var(--white);display:flex;align-items:center;justify-content:center;gap:6px;font-size:10px;font-weight:700;color:#1a2a7a}
.footer{left:50px;top:1110px;width:929px;height:49px;border-radius:6px;background:linear-gradient(var(--silver-top),var(--silver-bot));display:flex;align-items:center;justify-content:space-between;padding:0 16px 0 26px;font-size:12px;letter-spacing:1px;color:#333}
.footer .mark{font-family:"Questrial",sans-serif;font-size:22px;color:#4a4a4a;display:flex;align-items:center;gap:6px}
.footer .mark span{width:16px;height:16px;border-radius:50%;background:var(--red)}
</style>
</head>
<body>
<div class="abs backdrop"></div>

<header class="abs masthead"></header>
<div class="abs brand"><span class="brand-dot"></span>VELTRIX</div>
<div class="abs social feed" role="img" aria-label="News feed link"></div>
<div class="abs social one" role="img" aria-label="Social network link"></div>
<div class="abs social two" role="img" aria-label="Social network link"></div>
<a class="abs callout" href="tel:0000000000">
  <svg width="16" height="26" viewBox="0 0 16 26"><rect x="1" y="1" width="14" height="24" rx="5" fill="#dfe" stroke="#fff"/><rect x="5" y="5" width="6" height="9" rx="2" fill="#2bb24c"/></svg>
  000-000-0000
</a>

<nav class="abs nav">
  <a class="current" href="#">Home</a><a href="#">About Us</a><a href="#">Services</a><a href="#">Recent Jobs</a><a href="#">Experience</a><a href="#">Our Process</a><a href="#">Quotes</a><a href="#">FAQ</a><a href="#">Blog</a><a href="#">Contact Us</a>
</nav>

<div class="abs feature-photo" role="img" aria-label="Glowing copper cable ends on a dark background"></div>
<div class="abs slider"><div class="slide" role="img" aria-label="Slideshow photo: power plug with glowing fibres beside orange cabling in a switchboard"></div></div>
<div class="abs arrow" style="left:42px"><svg width="12" height="14" viewBox="0 0 12 14"><path d="M4 0h4v7h4L6 14 0 7h4z" fill="#333"/></svg></div>
<div class="abs arrow" style="left:587px"><svg width="12" height="14" viewBox="0 0 12 14"><path d="M4 14h4V7h4L6 0 0 7h4z" fill="#333"/></svg></div>

<div class="abs perk display" style="top:193px">24hours 7 days a week</div>
<div class="abs perk display" style="top:276px">No Call out Fee</div>
<div class="abs perk display" style="top:367px">Fixed Pricing</div>

<h1 class="abs section-title display" style="left:51px;top:478px;font-weight:400">Welcome &nbsp;to <span class="hl">Veltrix</span></h1>
<p class="abs copy" style="left:55px;top:516px;width:570px">Lorem Ipsum is simply dummy text of the printing and typesetting industry. Lorem Ipsum has been the industry's standard dummy text ever since the 1500s, when an unknown printer took a galley of type and scrambled it to make a type specimen book. It has survived not only five centuries, but</p>

<h2 class="abs section-title display" style="left:49px;top:616px;font-weight:400">Our <span class="hl">Services</span></h2>
<p class="abs copy" style="left:51px;top:664px;width:250px">Lorem Ipsum is simply dummy text of the printing and typeset-ting industry. Lorem Ipsum has been the industry's standard dummy text ever since the</p>
<div class="abs more" style="left:52px;top:781px">more <svg width="6" height="8"><path d="M0 0l6 4-6 4z" fill="#222"/></svg></div>

<h2 class="abs section-title display" style="left:366px;top:618px;font-weight:400">Our <span class="hl">Recent Jobs</span></h2>
<p class="abs copy" style="left:363px;top:664px;width:250px">Lorem Ipsum is simply dummy text of the printing and typeset-ting industry. Lorem Ipsum has been the industry's standard dummy text ever since the</p>
<div class="abs more" style="left:370px;top:781px">more <svg width="6" height="8"><path d="M0 0l6 4-6 4z" fill="#222"/></svg></div>

<section class="abs box" style="left:45px;top:773px;width:576px;height:274px;background:linear-gradient(#1e1e1e,#060606 40%,#000)">
  <h2 class="abs section-title display" style="left:14px;top:52px;font-weight:400">Testimonals</h2>
  <div class="abs avatar" style="top:94px"></div>
  <p class="abs copy" style="left:125px;top:105px;width:450px;color:var(--muted)">Lorem Ipsum is simply dummy text of the printing and type-setting industry. Lorem Ipsum has been the industry's stan-dard dummy text ever since the 1500s, when an unknown</p>
  <div class="abs avatar" style="left:18px;top:175px"></div>
  <p class="abs copy" style="left:124px;top:185px;width:450px;color:var(--muted)">Lorem Ipsum is simply dummy text of the printing and type-setting industry. Lorem Ipsum has been the industry's stan-dard dummy text ever since the 1500s, when an unknown</p>
  <div class="abs more" style="left:502px;top:243px">more <svg width="6" height="8"><path d="M0 0l6 4-6 4z" fill="#222"/></svg></div>
</section>

<form class="abs box" style="left:641px;top:489px;width:341px;height:280px">
  <div class="abs field" style="top:27px">Name</div>
  <div class="abs field" style="top:79px">E-Mail</div>
  <div class="abs field" style="top:131px;height:74px">Comment</div>
  <div class="abs btn" style="left:109px;top:227px;width:129px">Submit</div>
</form>

<div class="abs box" style="left:640px;top:772px;width:343px;height:103px;border-top:none;border-radius:0 0 14px 14px;background:#000">
  <div class="abs" style="left:12px;top:42px;width:207px;height:37px;border-radius:10px;background:var(--white)"></div>
  <div class="abs btn" style="left:230px;top:47px;width:101px">Search</div>
</div>

<section class="abs box" style="left:641px;top:888px;width:343px;height:156px">
  <h2 class="abs section-title display" style="left:45px;top:6px;font-weight:400">Latest <span class="hl">Blog Posts</span></h2>
  <p class="abs copy" style="left:37px;top:58px;width:290px;color:#888">Lorem Ipsum is simply dummy text of the printing and typesetting industry. Lorem Ipsum has been the industry's</p>
  <div class="abs more" style="left:248px;top:130px">more <svg width="6" height="8"><path d="M0 0l6 4-6 4z" fill="#222"/></svg></div>
</section>

<div class="abs payments" aria-label="Accepted payments"><span style="color:#c0392b">orbit pay</span><span>zenda</span></div>

<footer class="abs footer">
  <span>copyright@veltrix 2010</span>
  <span class="mark"><span></span>VELTRIX</span>
</footer>
</body>
</html>
```